QV - menu design

Hi,

We require elegant menu design for upscale restaurant. Please find attached the logo and the menu items for your reference.

for inspiration, this is a good website: -
http://www.platewhisper.example/bellfoldnotes/about.php

We are very much open for Menu Size suggestions.

unfortunately the place is going under renovation, we don't have updated images to it. the closest look and feel to our place is http://varnelo.example ..

we are also open for creative options on the shape, the styles, etc. as long as it represents the fine dine feel ...

Thanks ...

Dear All,

We wouldlike to extend our apology for not being able to provide feedbacks on everysingle design. We were extremely busy and we have multiple contests opensimultaneously which makes the process even harder.

However,we would like to thank you all for the efforts you have put into designingour menu. It is very much appreciated …

We wishyou all success in your design ventures and we are quite positive that we willbe working with many of you on many projects in the soon future. 

Thanks & Regards,

TLG Team...

 

 

 

Industry/Entity Type

Restaurant

Requirements
Must have
• Please ensure that there are 'some' images in the menu ... this is very important.
Should not have
• IMPORTANT: -

1. Please DO NOT insert any currency sign to the menu
2. Please keep the prices of the menu at the end of the menu items descriptions NOT beside the menu item names. The font of the price should be similar to the menu item description and please DO NOT bold the numbers. the prices should be subtle.

Thank you ...

```html
<!DOCTYPE html>
<html lang="en">
<head>
<meta charset="utf-8">
<title>QV – Menu Spread</title>
<link rel="stylesheet" href="https://fonts.googleapis.com/css2?family=Cinzel:wght@400;600&family=Arimo:wght@400&family=Josefin+Sans:wght@400&display=swap">
<style>
  :root{
    --stage:#7d8a91;
    --paper:#ffffff;
    --stripe:#f2ece3;
    --stripe-edge:#fbf8f4;
    --heading:#8a5a3a;
    --ink:#4a4540;
    --muted:#8b847c;
    --band:rgba(120,90,60,.72);
    --band-text:#ffffff;
    --logo:#2f2f2f;
    --fold:rgba(0,0,0,.10);
  }
  *{box-sizing:border-box;margin:0;padding:0}
  html,body{width:1200px;height:927px;overflow:hidden}
  body{background:var(--stage);font-family:"Arimo",Arial,sans-serif;color:var(--ink);position:relative}

  .brand{position:absolute;top:38px;left:0;width:1200px;text-align:center;
    font-family:"Josefin Sans",Arial,sans-serif;font-weight:400;color:var(--logo);
    font-size:70px;letter-spacing:14px;line-height:1}
  .caption{position:absolute;top:815px;left:0;width:1200px;text-align:center;
    font-family:"Arimo",Arial,sans-serif;color:#fff;font-size:30px}

  .spread{position:absolute;left:38px;top:167px;width:1127px;height:607px;
    display:flex;background:var(--paper);box-shadow:0 6px 14px rgba(0,0,0,.25)}
  .panel{position:relative;width:25%;height:100%;overflow:hidden;background:var(--paper)}
  .panel + .panel{box-shadow:inset 10px 0 14px -8px var(--fold)}
  .stripe{position:absolute;top:0;bottom:0;left:14%;right:14%;
    background:linear-gradient(90deg,var(--stripe-edge),var(--stripe) 20%,var(--stripe) 80%,var(--stripe-edge))}

  .menu{position:absolute;top:30px;left:8%;right:8%;text-align:center}
  .section-title{font-family:"Cinzel",Georgia,serif;font-weight:400;color:var(--heading);font-size:15px;letter-spacing:1px;margin:2px 0 6px}
  .item{margin-bottom:8px}
  .item-name{font-family:"Cinzel",Georgia,serif;color:var(--heading);font-size:12.5px;line-height:1.15}
  .item-desc{font-size:6.6px;line-height:1.35;color:var(--ink)}
  .item-price{font-size:7px;color:var(--muted)}
  .gap{height:10px}

  .cols{display:flex;gap:10px;text-align:center}
  .cols .col{flex:1}
  .small .item{margin-bottom:5px}
  .small .item-name{font-size:7.5px}
  .small .item-desc{font-size:5.6px}
  .small .item-price{font-size:5.6px}
  .list{font-size:5.6px;line-height:1.45;color:var(--ink);margin-bottom:5px}

  .photo{position:absolute;left:0;right:0;bottom:0}
  .band{position:absolute;left:0;right:0;top:545px;height:30px;background:var(--band);
    color:var(--band-text);font-family:"Josefin Sans",Arial,sans-serif;font-size:13px;letter-spacing:1px;
    display:flex;align-items:center;justify-content:center;text-transform:uppercase}

  .photo-salad{height:110px;background:radial-gradient(ellipse at 40% 55%,#e9e4c8,#c9c48e 45%,#f4f1ea 80%)}
  .photo-coffee{height:135px;background:linear-gradient(90deg,#f3efe8,#e8dccb 30%,#5a3b27 55%,#d9b894 80%,#f3efe8)}
  .photo-plate{top:0;background:linear-gradient(180deg,#f1ece4 0%,#e9e2d6 35%,#d9cdb8 55%,#e58a55 72%,#c8b89a 88%,#efe8dc 100%)}
  .photo-sandwich{height:120px;background:radial-gradient(ellipse at 55% 60%,#d8b27c,#e6d2ae 45%,#f5f1ea 80%)}

  .cover-brand{position:absolute;top:28px;left:0;right:0;text-align:center;
    font-family:"Josefin Sans",Arial,sans-serif;color:var(--logo);font-size:40px;letter-spacing:8px}
</style>
</head>
<body>
  <div class="brand">QV</div>

  <main class="spread">
    <!-- Soup & Salads -->
    <section class="panel panel-soup">
      <div class="stripe"></div>
      <div class="menu">
        <h2 class="section-title">Soup</h2>
        <div class="item"><div class="item-name">Bouillabaisse</div><div class="item-desc">Traditional French seafood soup, with saffron and fennel</div><div class="item-price">119</div></div>
        <div class="item"><div class="item-name">Barley Soup</div><div class="item-desc">With fresh vegetables, tomato broth and a hint of garlic oil</div><div class="item-price">49</div></div>
        <div class="item"><div class="item-name">Beef Chili</div><div class="item-desc">Served with Arabic bread, fresh guacamole and spicy black beans</div><div class="item-price">69</div></div>
        <div class="gap"></div>
        <h2 class="section-title">Salads</h2>
        <div class="item"><div class="item-name">Vegetarian Salad</div><div class="item-desc">Fresh green leaves, cherry tomatoes, carrots, cucumber, green apple and toasted pine nuts with house dressing</div><div class="item-price">59</div></div>
        <div class="item"><div class="item-name">Sweet Gorgonzola<br>Cheese Salad</div><div class="item-desc">Fresh green leaves, gorgonzola cheese, fresh pears, walnuts, garlic croutons and honey dressing</div><div class="item-price">69</div></div>
        <div class="item"><div class="item-name">Beef Sirloin Salad</div><div class="item-desc">Fresh green leaves, beef sirloin strips, roasted peppers and light pesto sauce</div><div class="item-price">79</div></div>
        <div class="item"><div class="item-name">Tandoori Chicken Salad</div><div class="item-desc">Fresh green leaves, tandoori chicken, mango, green grapes and crispy onion with yogurt sauce</div><div class="item-price">69</div></div>
        <div class="item"><div class="item-name">Sea Food Salad</div><div class="item-desc">Fresh green leaves, steamed seafood, black olives, celery and lemon dressing</div><div class="item-price">89</div></div>
        <div class="item"><div class="item-name">Fresh Tuna Salad</div><div class="item-desc">Fresh green leaves, seared tuna, boiled egg, capers and lemon dressing</div><div class="item-price">69</div></div>
      </div>
      <div class="photo photo-salad" role="img" aria-label="Photo of a chicken salad bowl with egg slices"></div>
      <div class="band">Soup &amp; Salads</div>
    </section>

    <!-- Desserts & Beverages -->
    <section class="panel panel-desserts">
      <div class="stripe"></div>
      <div class="menu small">
        <div class="cols">
          <div class="col">
            <h2 class="section-title">Desserts</h2>
            <div class="item"><div class="item-name">Amaretto Tiramisu</div><div class="item-price">39</div></div>
            <div class="item"><div class="item-name">Meringata</div><div class="item-desc">Layered meringue with vanilla cream, berries and dark chocolate</div><div class="item-price">39</div></div>
            <div class="item"><div class="item-name">Virgin Parfait</div><div class="item-desc">Fresh passion fruit, lime and vanilla syrup</div><div class="item-price">29</div></div>
            <div class="item"><div class="item-name">Very Berry</div><div class="item-desc">Mixed berries, cranberry juice and mint</div><div class="item-price">29</div></div>
            <div class="item"><div class="item-name">Third Wave</div><div class="item-desc">Apple, pineapple and strawberry juice with almond syrup</div><div class="item-price">29</div></div>
            <div class="item"><div class="item-name">Melon Mint</div><div class="item-desc">Fresh melon, apple juice and mint</div><div class="item-price">29</div></div>
            <div class="item"><div class="item-name">Raspberry Spritzer</div><div class="item-desc">Fresh raspberry, lemon and soda</div><div class="item-price">29</div></div>
            <div class="item-name">Ice Teas</div>
            <div class="list">Peach Ice Tea 19<br>Lemon Ice Tea 19<br>Mint Ice Tea 19<br>Red Berry Ice Tea 19</div>
            <div class="item-name">Hot Beverages</div>
            <div class="list">English Breakfast 15<br>Pure Green Tea 15<br>Earl Grey 15<br>Jasmine 15<br>Peppermint 15</div>
            <div class="item-name">Milk Shakes</div>
            <div class="list">Vanilla 25<br>Chocolate 25<br>Strawberry 25</div>
          </div>
          <div class="col">
            <div class="item"><div class="item-name">Fresh Fruit Tart</div><div class="item-desc">Choice of our home made cakes</div><div class="item-price">35</div></div>
            <div class="item"><div class="item-name">Cold Beverages / Cocktails</div><div class="item-desc">Lemon with mint</div><div class="item-price">25</div></div>
            <div class="item"><div class="item-name">Affogato</div><div class="item-desc">Scoop of vanilla ice cream topped with espresso</div><div class="item-price">29</div></div>
            <div class="item"><div class="item-name">Blue Lemonade</div><div class="item-desc">Fresh lemon juice, mint and blue syrup</div><div class="item-price">29</div></div>
            <div class="item"><div class="item-name">Mango Bomba</div><div class="item-desc">Fresh passion fruit, mango juice and peach</div><div class="item-price">29</div></div>
            <div class="item"><div class="item-name">Sunrise</div><div class="item-desc">Orange juice, pineapple juice and grenadine</div><div class="item-price">29</div></div>
            <div class="item"><div class="item-name">Milk Shake Classic</div><div class="item-desc">Vanilla ice cream, banana and dates</div><div class="item-price">29</div></div>
            <div class="item-name">Fresh Juices</div>
            <div class="list">Orange 25<br>Lemon 25<br>Carrot 25<br>Watermelon 25</div>
            <div class="item-name">Coffee</div>
            <div class="list">Espresso 15<br>Cappuccino 19<br>Latte 19<br>Americano 15<br>Hot Chocolate 19</div>
            <div class="item-name">Iced Coffee</div>
            <div class="list">Iced Latte 22<br>Frappe 25</div>
          </div>
        </div>
      </div>
      <div class="photo photo-coffee" role="img" aria-label="Photo of a coffee cup, coffee beans and small tarts"></div>
      <div class="band">Desserts &amp; Beverages</div>
    </section>

    <!-- Cover / feature photo -->
    <section class="panel panel-cover">
      <div class="photo photo-plate" role="img" aria-label="Photo of smoked salmon with potato rosti, lemon and a dip bowl beside a glass"></div>
      <div class="cover-brand">QV</div>
    </section>

    <!-- Breakfast & Sandwiches -->
    <section class="panel panel-breakfast">
      <div class="stripe"></div>
      <div class="menu">
        <h2 class="section-title">The Breakfast</h2>
        <div class="item"><div class="item-name">Butter Croissant</div><div class="item-desc">Served plain with a selection of jams, vanilla custard cream or chocolate</div><div class="item-price">29</div></div>
        <div class="item"><div class="item-name">Cheese Croissant</div><div class="item-desc">Crusty freshly baked with cheese filling</div><div class="item-price">29</div></div>
        <div class="item"><div class="item-name">Daily Fresh Eggs</div><div class="item-desc">A choice of poached, scrambled or fried eggs served with toast and grilled tomato</div><div class="item-price">39</div></div>
        <div class="item"><div class="item-name">Healthy Time</div><div class="item-desc">One choice of hot beverage with fruit salad, natural yogurt and whole wheat toast</div><div class="item-price">59</div></div>
        <div class="item"><div class="item-name">Energy Time</div><div class="item-desc">One choice of hot beverage with muffins, poached egg and crispy beef bacon</div><div class="item-price">59</div></div>
        <div class="item"><div class="item-name">QV Morning Time</div><div class="item-desc">One choice of hot beverage with scones, smoked salmon, grilled sausages and juice</div><div class="item-price">79</div></div>
        <div class="item"><div class="item-name">The Arabic Breakfast</div><div class="item-desc">Zaatar sandwich and cheese sandwich served with labneh and olives</div><div class="item-price">49</div></div>
        <div class="gap"></div>
        <h2 class="section-title">The Sandwiches</h2>
        <div class="item"><div class="item-desc">Grilled vegetables sandwich with fresh goat cheese and pesto</div><div class="item-price">49</div></div>
        <div class="item"><div class="item-desc">Butterfish burger with fresh tomato, iceberg and tartare sauce</div><div class="item-price">59</div></div>
        <div class="item"><div class="item-desc">Turkish tuna sandwich with red onion, olives and capers</div><div class="item-price">49</div></div>
        <div class="item"><div class="item-desc">Beef sirloin steak sandwich with grain mustard and parmesan</div><div class="item-price">69</div></div>
        <div class="item"><div class="item-desc">The traditional club sandwich served with french fries</div><div class="item-price">59</div></div>
      </div>
      <div class="photo photo-sandwich" role="img" aria-label="Photo of a filled baguette sandwich"></div>
      <div class="band">Breakfast &amp; Sandwiches</div>
    </section>
  </main>

  <div class="caption">Spread Page</div>
</body>
</html>
```